Real Estate Webpage Design

We have an existing website: brindlewoodhomes.com.au
We focus customised service mainly on Property Management and second-hand property sales.
We are not entirely happy about the current design and layout can stay roughly the same as the back end coding is linked to a CRM system.
We would like to see the design are more reachable to our clients and appearing.
Please check our Website Design Draft for more details.

Industry/Entity Type

Real estate Agency

Number of Pages Required

5+ page

Font styles to use
Sans Serif

Colors

Designer to choose colors to be used in the design.

```html
<!DOCTYPE html>
<html lang="en">
<head>
<meta charset="utf-8">
<title>Brindlewood Homes – Find your dream home</title>
<link href="https://fonts.googleapis.com/css2?family=Montserrat:wght@500;600;700&family=Roboto:wght@400;500;700&display=swap" rel="stylesheet">
<style>
:root{
  --brand:#fbb713;
  --ink:#1b1b1b;
  --body:#6b6b6b;
  --muted:#9a9a9a;
  --panel:#f0eeee;
  --band:#f3f3f3;
  --line:#dcdcdc;
  --white:#ffffff;
}
*{box-sizing:border-box;margin:0;padding:0}
html,body{width:1200px;height:4286px;overflow:hidden;background:var(--white)}
body{position:relative;font-family:'Roboto',sans-serif;color:var(--ink)}
.abs{position:absolute}
.h-sec{font-family:'Montserrat',sans-serif;font-weight:700;font-size:32px;color:var(--ink)}
.btn{position:absolute;background:var(--brand);color:var(--ink);font-weight:700;font-size:16px;display:flex;align-items:center;justify-content:center}
.photo{position:absolute}
.text{font-size:13.5px;line-height:23px;color:var(--body)}

/* header */
.header{left:0;top:0;width:1200px;height:75px;background:var(--white)}
.brand-name{left:86px;top:14px;display:flex;align-items:center;gap:10px;white-space:nowrap;font-family:'Montserrat',sans-serif;font-weight:700;font-size:22px;color:var(--brand)}
.brand-name .mark{width:40px;height:40px;border:5px solid var(--brand);flex:none}
.nav a{position:absolute;top:27px;font-size:14px;color:#333;text-decoration:none;line-height:18px;white-space:nowrap}
.nav a.active{color:var(--brand)}
.nav a.hl{background:var(--brand);padding:0 3px}

/* hero */
.hero{left:0;top:75px;width:1200px;height:531px;background:linear-gradient(160deg,#26406f 0%,#5d6f86 35%,#8b8b84 60%,#4e5b3a 100%)}
.hero-title{left:0;top:255px;width:1200px;text-align:center;font-family:'Montserrat',sans-serif;font-weight:600;font-size:46px;color:var(--white)}
.hero-sub{left:0;top:322px;width:1200px;text-align:center;font-size:17px;color:#eee}

/* about */
.about-h{left:85px;top:738px;font-family:'Montserrat',sans-serif;font-weight:700;font-size:33px;line-height:38px}
.about-p{left:85px;top:835px;width:500px}
.about-p p{margin-bottom:12px}
.frame{left:935px;top:689px;width:178px;height:451px;background:var(--brand)}

.service-h{left:0;top:1213px;width:1200px;text-align:center}
.panel{position:absolute;background:var(--panel)}
.panel h3{position:absolute;font-family:'Montserrat',sans-serif;font-weight:600;font-size:22px}
.panel .text{position:absolute;width:320px}

/* listings */
.band{left:0;top:2100px;width:1200px;height:446px;background:var(--band)}
.week-h{left:0;top:2175px;width:1200px;text-align:center}
.tabs{left:301px;top:2238px;width:596px;height:58px;border:1px solid var(--brand);display:flex;background:var(--white)}
.tabs span{flex:1;display:flex;align-items:center;justify-content:center;font-size:16px;color:#444;position:relative}
.tabs span+span::before{content:"";position:absolute;left:0;top:14px;height:30px;border-left:1px solid var(--brand)}
.tabs .on{background:var(--brand);color:var(--ink);font-weight:700}
.card{position:absolute;top:2331px;width:324px;height:403px;background:var(--white);box-shadow:0 4px 18px rgba(0,0,0,.08)}
.card .img{position:absolute;left:0;top:0;width:324px;height:215px}
.card .price{position:absolute;left:26px;top:155px;font-size:24px;font-weight:700;color:var(--white)}
.card .loc{position:absolute;left:28px;top:195px;width:132px;height:35px;background:var(--white);color:var(--brand);font-weight:700;font-size:17px;display:flex;align-items:center;justify-content:center}
.card h4{position:absolute;left:26px;top:244px;font-family:'Montserrat',sans-serif;font-weight:600;font-size:16.5px;white-space:nowrap}
.card .meta{position:absolute;left:26px;font-size:12px;font-weight:700;color:#666;display:flex;align-items:center;gap:8px}
.card .feat{position:absolute;left:26px;top:357px;font-size:12px;color:#666;display:flex;gap:16px}
.card .feat i{display:inline-block;width:18px;height:13px;border:2px solid var(--brand);margin-right:8px;vertical-align:middle}

/* contact */
.touch-h{left:85px;top:3050px;font-family:'Montserrat',sans-serif;font-weight:700;font-size:34px;letter-spacing:.5px}
.field{position:absolute;border:1px solid var(--line);font-size:12px;color:#aaa;padding:16px 18px}

/* testimonial */
.testi{left:0;top:3405px;width:1200px;height:406px;background:linear-gradient(180deg,#3f4446,#2a2f31 60%,#454a49)}
.testi-h{left:0;top:3480px;width:1200px;text-align:center;font-family:'Montserrat',sans-serif;font-weight:700;font-size:31px;color:var(--white)}
.quote-text{left:240px;top:3650px;width:720px;text-align:center;font-size:13.5px;line-height:23px;font-weight:700;color:var(--white)}
.quote-by{left:0;top:3706px;width:1200px;text-align:center;font-size:17px;font-weight:700;color:var(--white)}
.arrow{position:absolute;width:54px;height:54px;border-radius:50%;display:flex;align-items:center;justify-content:center;font-size:24px}

/* footer */
.f-h{position:absolute;top:3892px;font-family:'Montserrat',sans-serif;font-weight:700;font-size:17px;color:var(--brand)}
.f-list{position:absolute;list-style:none;font-size:14px;color:#444}
.f-list li{height:31.6px}
.f-contact{position:absolute;left:651px;font-size:13.5px;line-height:21px;color:#444;display:flex;gap:10px}
.social{position:absolute;top:3937px;width:40px;height:40px;border-radius:50%;border:1.5px solid #333}
.rule{left:86px;top:4200px;width:1027px;border-top:1px solid #ccc}
.bottom{position:absolute;top:4220px;font-size:13.5px;color:#333;white-space:nowrap}
</style>
</head>
<body>

<header class="abs header">
  <div class="abs brand-name"><span class="mark"></span>Brindlewood Homes</div>
  <nav class="nav">
    <a class="active" style="left:448px">Home</a>
    <a style="left:507px">About us ⌄</a>
    <a style="left:599px">Landlord ⌄</a>
    <a style="left:691px">Tenant ⌄</a>
    <a class="hl" style="left:765px">Make a Switch</a>
    <a style="left:892px">Property Sales ⌄</a>
    <a class="hl" style="left:1013px">Appraisal now</a>
  </nav>
</header>

<section>
  <div class="abs hero" role="img" aria-label="Photo of apartment buildings with lawn and decorative colourful shapes"></div>
  <h1 class="abs hero-title">Find your dream home with Brindlewood</h1>
  <p class="abs hero-sub">Your local real estate property group</p>
  <a class="btn" style="left:499px;top:371px;width:203px;height:57px">Request An Appraisal</a>
</section>

<section>
  <h2 class="abs about-h">Brindlewood –<br>Built around “the home”</h2>
  <div class="abs about-p text">
    <p>Brindlewood Homes is about “the home, the house”: buying a property is one of the most expensive expenses and important assets for people. Brindlewood is a real estate company located in Ferncliff, Canberra.</p>
    <p>Being a portfolio sales agent and property manager, coupled with our high-profile international real estate experience, Brindlewood is considered a market leader on the cutting edge with deep industry knowledge, ranging from</p>
  </div>
  <a class="btn" style="left:85px;top:1020px;width:203px;height:57px">Contact With Us</a>
  <div class="abs frame"></div>
  <div class="photo" style="left:646px;top:719px;width:439px;height:391px;background:linear-gradient(180deg,#8fb6e8,#d9dde2 55%,#7d8a6e)" role="img" aria-label="Photo of a curved high-rise apartment tower"></div>
  <div class="photo" style="left:0;top:1098px;width:110px;height:168px;background:radial-gradient(circle at 40% 45%,#a8c96a,#6b8a3a 50%,rgba(255,255,255,0) 72%)" role="img" aria-label="Illustration of flowers on a rock"></div>
</section>

<section>
  <h2 class="abs h-sec service-h">Our service</h2>
  <div class="photo" style="left:86px;top:1285px;width:588px;height:349px;background:linear-gradient(180deg,#cfd8d4,#b8c3bd 40%,#2f49b8 62%,#6a8b45)" role="img" aria-label="Photo of an apartment swimming pool"></div>
  <div class="panel" style="left:700px;top:1285px;width:413px;height:349px">
    <h3 style="left:49px;top:40px">Property Management</h3>
    <p class="text" style="left:49px;top:88px">Lorem Ipsum is simply dummy text of the printing and typesetting industry. Lorem Ipsum has been the industry's standard dummy text ever since the 1500s, when an unknown printer took a galley of type and scrambled it to make a type specimen book.</p>
  </div>
  <a class="btn" style="left:749px;top:1526px;width:203px;height:57px">Request An Appraisal</a>

  <div class="panel" style="left:85px;top:1667px;width:411px;height:352px">
    <h3 style="left:47px;top:40px">Property sales</h3>
    <p class="text" style="left:47px;top:88px">Lorem Ipsum is simply dummy text of the printing and typesetting industry. Lorem Ipsum has been the industry's standard dummy text ever since the 1500s, when an unknown printer took a galley of type and scrambled it to make a type specimen book.</p>
  </div>
  <a class="btn" style="left:132px;top:1911px;width:204px;height:57px">Request An Appraisal</a>
  <div class="photo" style="left:526px;top:1667px;width:587px;height:352px;background:linear-gradient(160deg,#e3e5e6,#8fb0d8 45%,#c9c9c6 70%,#5d6a48)" role="img" aria-label="Photo of a modern house porch under a cloudy sky"></div>
</section>

<section>
  <div class="abs band"></div>
  <h2 class="abs h-sec week-h">Property of the week</h2>
  <div class="abs tabs"><span class="on">For Lease</span><span>For Sales</span><span>Sold</span><span>Leased</span></div>

  <article class="card" style="left:86px">
    <div class="img" role="img" aria-label="Photo of a two-storey house with garages" style="background:linear-gradient(180deg,#4e78c4,#b9a6a5 50%,#4a4c50)"></div>
    <div class="price">$1400 pw</div><div class="loc">Red Hill</div>
    <h4>9 Ashgrove Street Red Hill</h4>
    <div class="meta" style="top:284px">★ Add to favourites</div>
    <div class="meta" style="top:310px">✉ Email to agents</div>
    <div class="feat"><span><i></i>Beds 4</span><span><i></i>Baths 2</span><span><i></i>Parking 2</span></div>
  </article>
  <article class="card" style="left:438px">
    <div class="img" role="img" aria-label="Photo of an apartment living room" style="background:linear-gradient(180deg,#c9ccce,#8a8682 55%,#3d3633)"></div>
    <div class="price">$560 pw</div><div class="loc">Braddon</div>
    <h4>215/2 Tallis Street Braddon</h4>
    <div class="meta" style="top:284px">★ Add to favourites</div>
    <div class="meta" style="top:310px">✉ Email to agents</div>
    <div class="feat"><span><i></i>Beds 1</span><span><i></i>Baths 1</span><span><i></i>Parking 1</span></div>
  </article>
  <article class="card" style="left:789px">
    <div class="img" role="img" aria-label="Photo of a garden entrance with hedges" style="background:linear-gradient(180deg,#7ea0cc,#4f6f3a 45%,#3b4e2c)"></div>
    <div class="price">$1300 pw</div><div class="loc">Griffith</div>
    <h4>1 Wren Street Griffith</h4>
    <div class="meta" style="top:284px">★ Add to favourites</div>
    <div class="meta" style="top:310px">✉ Email to agents</div>
    <div class="feat"><span><i></i>Beds 4</span><span><i></i>Baths 2</span><span><i></i>Parking 3</span></div>
  </article>
  <a class="btn" style="left:499px;top:2782px;width:203px;height:57px">View More</a>
</section>

<section>
  <svg class="abs" style="left:85px;top:3004px" width="42" height="33" viewBox="0 0 42 33"><rect x="1" y="1" width="40" height="31" rx="3" fill="#fbb713"/><path d="M2 4 L21 18 L40 4" stroke="#fff" stroke-width="3" fill="none"/></svg>
  <h2 class="abs touch-h">Get In Touch With Us</h2>
  <p class="abs text" style="left:85px;top:3105px;width:460px">For more info or inquiry about our property and pricing please feel free to get in touch with us.</p>
  <div class="photo" style="left:86px;top:3162px;width:367px;height:166px;background:radial-gradient(ellipse at 50% 60%,#4f9a6a,#8fae7a 45%,rgba(255,255,255,0) 72%)" role="img" aria-label="Illustration of plants and stones"></div>

  <div class="field" style="left:612px;top:3004px;width:243px;height:53px">First name</div>
  <div class="field" style="left:869px;top:3004px;width:244px;height:53px">Last name</div>
  <div class="field" style="left:612px;top:3073px;width:243px;height:54px">Phone No.</div>
  <div class="field" style="left:869px;top:3073px;width:244px;height:54px">Email</div>
  <div class="field" style="left:612px;top:3142px;width:501px;height:98px">Message</div>
  <a class="btn" style="left:612px;top:3265px;width:137px;height:56px">Submit</a>
</section>

<section>
  <div class="abs testi" role="img" aria-label="Blurred photo of an interior"></div>
  <h2 class="abs testi-h">What’s Our People Says</h2>
  <div class="abs" style="left:570px;top:3560px;font-family:'Montserrat',sans-serif;font-weight:700;font-size:100px;line-height:100px;color:#ddd">“</div>
  <p class="abs quote-text">Maren is my best property manager! Always happy to response my queries and keep us well informed at all<br>stage.&nbsp; I will definitely recommend her to my friends.</p>
  <p class="abs quote-by">- l. ortega</p>
  <div class="arrow" style="left:86px;top:3646px;background:#8a8d8e;color:#555">‹</div>
  <div class="arrow" style="left:1060px;top:3646px;background:#fff;color:#333">›</div>
</section>

<footer>
  <div class="abs brand-name" style="top:3898px"><span class="mark"></span>Brindlewood Homes</div>
  <p class="abs text" style="left:85px;top:3972px;width:320px;color:#555">Lorem Ipsum is simply dummy text of the printing and typesetting industry. Lorem Ipsum has been the industry's standard dummy text ever since the 1500s....</p>

  <div class="f-h" style="left:471px">Sitemap</div>
  <ul class="f-list" style="left:471px;top:3936px">
    <li>Home</li><li>About us</li><li>Landlord</li><li>Tenant</li><li>Make a Switch</li><li>Property Sales</li><li>Appraisal now</li>
  </ul>

  <div class="f-h" style="left:651px">Contact Us</div>
  <div class="f-contact" style="top:3936px"><span style="color:#333">●</span><span>18/4 Marlow Crescent,<br>Ferncliff, ACT, 2914</span></div>
  <div class="f-contact" style="top:3995px"><span style="color:#333">☎</span><span>02 5550 1184<br>02 5550 2267</span></div>
  <div class="f-contact" style="top:4050px"><span style="color:#333">✉</span><span>info@brindlewood.com</span></div>

  <div class="f-h" style="left:910px">Follow Us On</div>
  <div class="social" style="left:912px;background:var(--brand);border-color:var(--brand)" aria-label="Social profile"></div>
  <div class="social" style="left:965px" aria-label="Social profile"></div>
  <div class="social" style="left:1018px" aria-label="Social profile"></div>
  <div class="social" style="left:1072px" aria-label="Social profile"></div>

  <div class="abs rule"></div>
  <div class="bottom" style="left:86px">Copyright 2022 Brindlewood Homes.All right Reserved.</div>
  <div class="bottom" style="left:602px">Privacy</div>
  <div class="bottom" style="left:671px">Complaint Handling &amp; Dispute Resolution</div>
  <div class="bottom" style="left:959px">Due Diligence Checklist</div>
</footer>

</body>
</html>
```